Postcard Design

Income tax servicesOver 20 years experienceBusiness and Personal Tax ReturnsAll State ReturnsFree Electronic FilingI would like a simple map showing how to get to my house.reasons to use a tax preparerYou don’t have to keep up with the many tax law changes or understand complicated tax law.Your time is worth money – add up the hours you would spend doing it yourself and calculate what that’s worth.A tax program in a box cannot represent you in an audit.A tax professional can answer your questions to help you make smarter tax-saving decisions.It gives you peace of mind knowing that a professional is taking care of it.It can save you money – if your tax preparer finds even one significant deduction or tax credit you may have missed, it can easily cover the cost to have them prepared.Going to be targeting the area within 2 square miles of my home office so would like to promote proximity to the possible clients

```html
<!DOCTYPE html>
<html lang="en">
<head>
<meta charset="utf-8">
<title>Income Tax Services Postcard</title>
<link rel="stylesheet" href="https://fonts.googleapis.com/css2?family=Anton&family=Open+Sans:wght@300;400;600;700&family=Roboto+Condensed:wght@300;700&display=swap">
<style>
  :root {
    --backdrop: #3b2b21;
    --card: #ffffff;
    --brand-blue: #1a72b8;
    --band-deep: #16489a;
    --band-light: #2280c9;
    --accent-orange: #f5a11a;
    --accent-gold: #f9c34a;
    --ink: #1d1d1d;
    --body-ink: #3a3a3a;
    --bullet: #1f6fc0;
    --map-base: #e9e7e2;
  }
  * { margin: 0; padding: 0; box-sizing: border-box; }
  html, body { width: 874px; height: 1200px; overflow: hidden; }
  body { background: var(--backdrop); position: relative; font-family: "Open Sans", sans-serif; }

  .postcard {
    position: absolute; left: 73px; width: 725px;
    background: var(--card); overflow: hidden;
    box-shadow: 0 6px 16px rgba(0,0,0,.5);
  }
  .postcard--front { top: 66px; height: 516px; }
  .postcard--back { top: 625px; height: 517px; }

  /* front */
  .hero-photo {
    position: absolute; left: 0; top: 0; width: 400px; height: 430px;
    background: radial-gradient(ellipse at 40% 30%, #f3f1ec 0%, #dcd8cf 55%, rgba(255,255,255,0) 100%),
                linear-gradient(160deg, #e2c07a 0%, #d8d3c8 45%, #f4f4f2 100%);
  }
  .experience-badge {
    position: absolute; left: 237px; top: 84px; width: 94px; height: 94px;
  }
  .stamp-label {
    position: absolute; left: 62px; top: 280px;
    transform: rotate(-9deg); transform-origin: left top;
    color: #fff;
  }
  .stamp-label .name { font-family: "Anton", sans-serif; font-size: 40px; letter-spacing: .5px; line-height: 1; }
  .stamp-label .email { font-family: "Open Sans", sans-serif; font-weight: 700; font-size: 15px; margin-left: 32px; }

  .firm-name {
    position: absolute; right: 44px; top: 20px;
    font-family: "Open Sans", sans-serif; font-weight: 700; font-size: 26px; color: var(--ink);
    display: flex; align-items: center; gap: 8px;
  }
  .firm-name .dot { width: 14px; height: 14px; border-radius: 50%; background: var(--ink); }

  .headline {
    position: absolute; right: 38px; top: 100px; text-align: right;
    font-family: "Anton", sans-serif; color: var(--brand-blue);
    font-size: 62px; line-height: 60px; letter-spacing: 1px;
  }
  .service-line {
    position: absolute; right: 38px; top: 242px; text-align: right;
    font-family: "Open Sans", sans-serif; font-weight: 300; color: var(--ink);
  }
  .service-line .small { font-size: 37px; line-height: 42px; display: block; }
  .service-line .large { font-size: 56px; line-height: 62px; display: block; }

  .band { position: absolute; left: 0; width: 725px; }
  .band--front { top: 396px; height: 120px; }
  .band--back { top: 393px; height: 124px; }

  .feature-list {
    position: absolute; left: 28px; top: 432px; list-style: none;
    font-family: "Anton", sans-serif; color: #fff; font-size: 28px; line-height: 36px; letter-spacing: .5px;
  }
  .feature-list li { display: flex; align-items: center; gap: 10px; }
  .feature-list svg { width: 24px; height: 24px; }

  .front-contact {
    position: absolute; right: 37px; top: 445px; text-align: right; color: #fff;
  }
  .front-contact .call { font-family: "Roboto Condensed", sans-serif; font-weight: 300; font-size: 22px; }
  .front-contact .call strong { font-weight: 700; font-size: 27px; letter-spacing: .5px; }
  .front-contact .web { font-family: "Open Sans", sans-serif; font-weight: 700; font-size: 17px; margin-top: 4px; }

  /* back */
  .area-map {
    position: absolute; inset: 0;
    background: linear-gradient(135deg, #eeece7 0%, var(--map-base) 60%, #dedcd5 100%);
  }
  .reasons-panel {
    position: absolute; left: 0; top: 0; width: 398px; height: 420px;
    background: #fff; border-bottom-right-radius: 20px;
  }
  .reasons-title {
    position: absolute; left: 16px; top: 18px; width: 367px; height: 34px;
    background: var(--brand-blue); color: #fff; border-radius: 17px;
    font-family: "Roboto Condensed", sans-serif; font-weight: 300; font-size: 23px;
    line-height: 34px; padding-left: 16px;
  }
  .reasons-list {
    position: absolute; left: 24px; top: 61px; width: 358px; list-style: none;
    font-size: 12.6px; line-height: 17px; color: var(--body-ink); text-align: justify;
  }
  .reasons-list li { position: relative; padding-left: 19px; margin-bottom: 10px; }
  .reasons-list li::before {
    content: ""; position: absolute; left: 0; top: 3px; width: 12px; height: 12px; border-radius: 50%;
    background: radial-gradient(circle at 35% 35%, #8cc3f0 0%, var(--bullet) 60%, #0e4a8c 100%);
  }

  .back-contact { position: absolute; left: 28px; top: 445px; color: #fff; }
  .back-contact .call { font-family: "Roboto Condensed", sans-serif; font-weight: 700; font-size: 18px; }
  .back-contact .call strong { font-size: 24px; }
  .back-contact .web { font-family: "Anton", sans-serif; font-size: 23px; letter-spacing: 1px; margin-top: 2px; }
  .back-signature { position: absolute; right: 43px; top: 437px; text-align: right; color: #fff; }
  .back-signature .name { font-family: "Anton", sans-serif; font-size: 33px; letter-spacing: 1px; line-height: 40px; }
  .back-signature .email { font-family: "Open Sans", sans-serif; font-weight: 700; font-size: 16px; margin-top: 2px; }
</style>
</head>
<body>

<section class="postcard postcard--front">
  <div class="hero-photo" role="img" aria-label="Photo of a wooden rubber stamp resting on a stack of tax papers"></div>
  <svg class="experience-badge" viewBox="0 0 94 94" aria-hidden="true">
    <circle cx="47" cy="47" r="46" fill="#e4e4e4"/>
    <circle cx="47" cy="47" r="30" fill="var(--accent-orange)"/>
  </svg>
  <div class="stamp-label">
    <div class="name">Daniel Reyes, CPA</div>
    <div class="email">email: reyestaxdesk@example.com</div>
  </div>

  <div class="firm-name"><span class="dot"></span>Tax Desk</div>

  <h1 class="headline">INCOME TAX<br>SERVICES</h1>
  <p class="service-line"><span class="small">business</span><span class="small">and personal</span><span class="large">tax returns</span></p>

  <svg class="band band--front" viewBox="0 0 725 120" preserveAspectRatio="none" aria-hidden="true">
    <defs>
      <linearGradient id="bandFront" x1="0" x2="1">
        <stop offset="0" stop-color="var(--band-deep)"/>
        <stop offset="1" stop-color="var(--band-light)"/>
      </linearGradient>
    </defs>
    <path d="M0 34 C200 8 430 40 725 10 L725 120 L0 120 Z" fill="url(#bandFront)"/>
    <path d="M0 30 C200 2 430 34 725 2 L725 9 C430 42 200 12 0 38 Z" fill="var(--accent-orange)"/>
    <path d="M380 30 C520 32 640 22 725 14 L725 18 C640 28 520 36 380 30 Z" fill="var(--accent-gold)"/>
  </svg>

  <ul class="feature-list">
    <li><svg viewBox="0 0 24 24"><path d="M2 13 L9 20 L22 4" fill="none" stroke="var(--accent-orange)" stroke-width="4" stroke-linecap="round" stroke-linejoin="round"/></svg>All State Returns</li>
    <li><svg viewBox="0 0 24 24"><path d="M2 13 L9 20 L22 4" fill="none" stroke="var(--accent-orange)" stroke-width="4" stroke-linecap="round" stroke-linejoin="round"/></svg>Free Electronic Filing</li>
  </ul>
  <div class="front-contact">
    <div class="call">Call to Daniel Reyes CPA: <strong>02-555-0148</strong></div>
    <div class="web">www.nearbytaxdesk.com</div>
  </div>
</section>

<section class="postcard postcard--back">
  <div class="area-map" role="img" aria-label="Street map of the neighbourhood with a pin marking the office at 4120 E Cedar Vista Ave"></div>
  <div class="reasons-panel"></div>
  <h2 class="reasons-title">REASONS TO USE A TAX PREPARER</h2>
  <ul class="reasons-list">
    <li>You don’t have to keep up with the many tax law changes or understand complicated tax law.</li>
    <li>Your time is worth money – add up the hours you would spend doing it yourself and calculate what that’s worth.</li>
    <li>A tax program in a box cannot represent you in an audit.</li>
    <li>A tax professional can answer your questions to help you make smarter tax-saving decisions.</li>
    <li>It gives you peace of mind knowing that a professional is taking care of it.</li>
    <li>It can save you money – if your tax preparer finds even one significant deduction or tax credit you may have missed, it can easily cover the cost to have them prepared.</li>
    <li>Going to be targeting the area within 2 square miles of my home office so would like to promote proximity to the possible clients</li>
  </ul>

  <svg class="band band--back" viewBox="0 0 725 124" preserveAspectRatio="none" aria-hidden="true">
    <defs>
      <linearGradient id="bandBack" x1="0" x2="1">
        <stop offset="0" stop-color="var(--band-deep)"/>
        <stop offset="1" stop-color="var(--band-light)"/>
      </linearGradient>
    </defs>
    <path d="M0 16 C220 40 450 -4 725 30 L725 124 L0 124 Z" fill="url(#bandBack)"/>
    <path d="M0 8 C220 34 450 -12 725 22 L725 30 C450 -4 220 42 0 16 Z" fill="var(--accent-orange)"/>
    <path d="M430 6 C560 4 650 12 725 20 L725 24 C650 16 560 8 430 6 Z" fill="var(--accent-gold)"/>
  </svg>

  <div class="back-contact">
    <div class="call">Call Now Today : <strong>602-555-0148</strong></div>
    <div class="web">www.nearbytaxdesk.com</div>
  </div>
  <div class="back-signature">
    <div class="name">Daniel Reyes, CPA</div>
    <div class="email">email: reyestaxdesk@example.com</div>
  </div>
</section>

</body>
</html>
```